8' X 8" convention booth design

I am requesting a design for a convention booth. This design must be created in Adobe Illustrator.
I sell insurance programs to the members of associations. My prospects that will see this booth are association professionals looking to select a provider of insurance benefits for their memberships. I would like my prospects to look at my booth, see our logo, understand what we do, and then show some icons highlighting the insurance products that we have available. Please feel free to add any pictures or anything you might find to make the booth more appealing, but are not necessary. I have attached a photo of a sample of the booth construction below for your review.
The booth is 8’ X 8’ in the front and will have two 1’ side panels on each side. The dimensions of the front graphics are 87.75” W X 87.75” H. Each of the two side panel is 12 W X 87.75” H. The total width of the design is 111.75”. The graphic should be designed to include the 12’ wrap around on each side.
I have attached two of our logos below. The attached KWR logo with the words "Affinity and Association Services" is the logo for the front of the booth. The plain KWR logo is for the top of the side panels.
For side panels, please put the KWR logo (with only the KWR letters) at the top and the words "Association Insurance" underneath the KWR logo. The Association Insurance letters should be vertical.
For the front of the booth, I would like to have the KWR logo somewhere prominent in your design. I do not want it too big, but would like people to notice my company logo and description line. Also on the front of the booth, please include the following information that describes my company:
Full Portfolio of Insurance Products
Brokerage with A-Rated insurance companies
Full-Service Administrator
State-of-the-Art Technologies
Multi-Channel Marketing
The header for this section of five bullets above can be Member Insurance Program Management.
Lastly, I have attached 14 other icons that represent the insurance products I am offering. Please place them in a grid, or some other creative way, and include the word I have used to name each icon below each icon. For example, please type the word Life under the Life icon in the design. If you are looking for a header for this section, it can be Insurance Products Thank you very much for your interest.
Target Market(s)
Association Executive Directors looking to offer valuable member benefits to their association membership.
Colors
Look and feel

```html
<!DOCTYPE html>
<html lang="en">
<head>
<meta charset="utf-8">
<title>KWR Affinity &amp; Association Services – Booth Graphic</title>
<link href="https://fonts.googleapis.com/css2?family=Montserrat:ital,wght@0,500;0,600;1,500&family=Roboto:wght@400;500&display=swap" rel="stylesheet">
<style>
  :root{
    --olive:#8c9b2b;
    --olive-dark:#5f6b1c;
    --olive-deep:#3d4512;
    --ink:#3a3a3a;
    --grey:#6b6b6b;
    --line:#cfcfcf;
    --paper:#ffffff;
    --stage:#1c1c1c;
  }
  *{box-sizing:border-box;margin:0;padding:0}
  html,body{width:1200px;height:675px;overflow:hidden;background:var(--stage)}
  .booth{position:absolute;left:192px;top:17px;width:816px;height:640px;display:flex;background:var(--paper)}
  .side-panel{position:relative;width:88px;height:100%;background:var(--paper);overflow:hidden}
  .side-panel .brand-mark{position:absolute;top:20px;left:0;width:100%;text-align:center;
    font-family:"Montserrat",sans-serif;font-weight:600;font-size:22px;color:var(--olive)}
  .side-panel .edge-band{position:absolute;top:70px;bottom:28px;width:22px;background:var(--olive)}
  .side-left .edge-band{left:0}
  .side-right .edge-band{right:0}
  .side-panel .vertical-title{position:absolute;left:50%;top:340px;transform:translate(-50%,-50%) rotate(-90deg);
    white-space:nowrap;font-family:"Montserrat",sans-serif;font-weight:500;font-size:19px;letter-spacing:3px;color:var(--ink)}
  .stripes{position:absolute;left:0;right:0;bottom:0;height:28px}
  .stripes span{position:absolute;left:0;right:0}
  .stripes .s1{bottom:16px;height:4px;background:var(--olive-deep)}
  .stripes .s2{bottom:0;height:12px;background:var(--olive)}

  .front{position:relative;width:640px;height:100%;border-left:1px solid #eee;border-right:1px solid #eee}
  .front-header{position:absolute;left:36px;top:18px;display:flex;align-items:center;gap:14px;height:50px}
  .front-header .brand-mark{font-family:"Montserrat",sans-serif;font-weight:600;font-size:34px;color:var(--olive)}
  .front-header .divider{width:10px;height:30px;border-left:2px solid var(--olive);border-right:2px solid var(--ink)}
  .front-header .tagline{font-family:"Montserrat",sans-serif;font-style:italic;font-weight:500;font-size:13px;letter-spacing:2px;color:var(--ink);text-transform:uppercase}

  .hero{position:absolute;left:0;top:80px;width:640px;height:270px}
  .hero-content{position:absolute;left:70px;top:168px;width:545px}
  .hero-title{font-family:"Montserrat",sans-serif;font-weight:600;font-size:20px;color:#fff;padding-bottom:6px;border-bottom:2px solid #fff;display:inline-block;white-space:nowrap}
  .benefits{margin-top:10px;display:grid;grid-template-columns:300px 237px;gap:6px 8px;list-style:none}
  .benefits li{background:#fff;height:22px;display:flex;align-items:center;padding-left:8px;gap:6px;
    font-family:"Roboto",sans-serif;font-size:11.5px;color:var(--ink);white-space:nowrap;overflow:hidden}
  .benefits li svg{flex:none}

  .products{position:absolute;left:70px;top:372px;width:560px}
  .products-title{font-family:"Montserrat",sans-serif;font-weight:600;font-size:19px;color:var(--ink);
    display:inline-block;padding-bottom:4px;border-bottom:2px solid var(--grey)}
  .icon-grid{margin-top:14px;display:grid;grid-template-columns:repeat(7,62px);gap:14px 14px}
  .icon-item{text-align:center;font-family:"Roboto",sans-serif;font-size:9.5px;line-height:1.15;color:var(--ink)}
  .icon-box{width:58px;height:58px;margin:0 auto 5px;border:1px solid var(--line);box-shadow:1px 1px 2px rgba(0,0,0,.18);
    display:flex;align-items:center;justify-content:center;background:#fff}
  .icon-box svg{width:40px;height:40px}
</style>
</head>
<body>
<main class="booth">

  <section class="side-panel side-left">
    <div class="brand-mark">KWR</div>
    <div class="edge-band"></div>
    <div class="vertical-title">ASSOCIATION INSURANCE</div>
    <div class="stripes"><span class="s1"></span><span class="s2"></span></div>
  </section>

  <section class="front">
    <header class="front-header">
      <div class="brand-mark">KWR</div>
      <div class="divider"></div>
      <div class="tagline">Affinity &amp; Association Services</div>
    </header>

    <svg class="hero" viewBox="0 0 640 270" preserveAspectRatio="none" role="img" aria-label="Photo of smiling colleagues giving a high five in an office, tinted olive green">
      <defs>
        <linearGradient id="heroTone" x1="0" y1="0" x2="1" y2="1">
          <stop offset="0" stop-color="#6f7a24"/>
          <stop offset=".5" stop-color="#4a5218"/>
          <stop offset="1" stop-color="#8c9b2b"/>
        </linearGradient>
      </defs>
      <path d="M0 0H640V230C460 262 240 275 0 262Z" fill="url(#heroTone)"/>
    </svg>

    <div class="hero-content">
      <h1 class="hero-title">Member Insurance Program Management</h1>
      <ul class="benefits">
        <li><svg width="9" height="9" viewBox="0 0 10 10"><path d="M5 0l1.5 3.4 3.5.3-2.7 2.3.8 3.5L5 7.6 1.9 9.5l.8-3.5L0 3.7l3.5-.3z" fill="var(--olive)"/></svg>Full Portfolio of Insurance Products</li>
        <li><svg width="9" height="9" viewBox="0 0 10 10"><path d="M5 0l1.5 3.4 3.5.3-2.7 2.3.8 3.5L5 7.6 1.9 9.5l.8-3.5L0 3.7l3.5-.3z" fill="var(--olive)"/></svg>State-of-the-Art Technologies</li>
        <li><svg width="9" height="9" viewBox="0 0 10 10"><path d="M5 0l1.5 3.4 3.5.3-2.7 2.3.8 3.5L5 7.6 1.9 9.5l.8-3.5L0 3.7l3.5-.3z" fill="var(--olive)"/></svg>Brokerage with A-Rated insurance companies</li>
        <li><svg width="9" height="9" viewBox="0 0 10 10"><path d="M5 0l1.5 3.4 3.5.3-2.7 2.3.8 3.5L5 7.6 1.9 9.5l.8-3.5L0 3.7l3.5-.3z" fill="var(--olive)"/></svg>Multi-Channel Marketing</li>
        <li><svg width="9" height="9" viewBox="0 0 10 10"><path d="M5 0l1.5 3.4 3.5.3-2.7 2.3.8 3.5L5 7.6 1.9 9.5l.8-3.5L0 3.7l3.5-.3z" fill="var(--olive)"/></svg>Full-Service Administrator</li>
      </ul>
    </div>

    <section class="products">
      <h2 class="products-title">Insurance Products</h2>
      <div class="icon-grid">
        <div class="icon-item"><div class="icon-box"><svg viewBox="0 0 40 40"><path d="M4 24l30-10c3-1 4 2 1 3L8 27z" fill="var(--olive)"/><path d="M16 20l-6-10h4l10 7zM14 25l-2 7h3l6-9z" fill="var(--olive-dark)"/></svg></div>Travel</div>
        <div class="icon-item"><div class="icon-box"><svg viewBox="0 0 40 40"><path d="M8 16a12 10 0 0124 0z" fill="var(--ink)"/><rect x="19" y="16" width="2" height="8" fill="var(--ink)"/><text x="8" y="36" font-family="Roboto,sans-serif" font-size="16" font-weight="500" fill="var(--olive)">$</text><rect x="22" y="24" width="8" height="12" fill="var(--ink)"/></svg></div>Business</div>
        <div class="icon-item"><div class="icon-box"><svg viewBox="0 0 40 40"><path d="M24 4l10 4v7c0 6-5 9-10 11-5-2-10-5-10-11V8z" fill="var(--olive)"/><path d="M5 28l3-6h16l3 6v6H5z" fill="var(--ink)"/><circle cx="10" cy="34" r="2.5" fill="#fff"/><circle cx="22" cy="34" r="2.5" fill="#fff"/></svg></div>Auto</div>
        <div class="icon-item"><div class="icon-box"><svg viewBox="0 0 40 40"><path d="M20 6L6 18h4v14h20V18h4z" fill="var(--olive)"/><rect x="17" y="22" width="6" height="10" fill="#fff"/></svg></div>Home</div>
        <div class="icon-item"><div class="icon-box"><svg viewBox="0 0 40 40"><rect x="8" y="5" width="22" height="28" fill="#fff" stroke="var(--ink)" stroke-width="2"/><path d="M12 12h14M12 18h14M12 24h9" stroke="var(--olive)" stroke-width="2"/></svg></div>Rx Cards</div>
        <div class="icon-item"><div class="icon-box"><svg viewBox="0 0 40 40"><rect x="16" y="6" width="18" height="26" fill="#fff" stroke="var(--ink)" stroke-width="2"/><path d="M14 12l8 3v6c0 5-4 8-8 10-4-2-8-5-8-10v-6z" fill="var(--olive)"/><path d="M12 22h4M14 20v4" stroke="#fff" stroke-width="2"/></svg></div>Health</div>
        <div class="icon-item"><div class="icon-box"><svg viewBox="0 0 40 40"><path d="M6 18a14 12 0 0128 0z" fill="var(--olive)"/><rect x="19" y="18" width="2" height="6" fill="var(--ink)"/><path d="M14 34c0-6 3-10 6-10s6 4 6 10z" fill="var(--ink)"/></svg></div>Financial<br>Wellness</div>

        <div class="icon-item"><div class="icon-box"><svg viewBox="0 0 40 40"><path d="M20 4l14 5v10c0 9-7 14-14 17-7-3-14-8-14-17V9z" fill="none" stroke="var(--ink)" stroke-width="2.5"/><ellipse cx="20" cy="19" rx="9" ry="5" fill="var(--olive)"/><circle cx="20" cy="19" r="3" fill="var(--ink)"/></svg></div>Vision</div>
        <div class="icon-item"><div class="icon-box"><svg viewBox="0 0 40 40"><path d="M20 4l14 5v10c0 9-7 14-14 17-7-3-14-8-14-17V9z" fill="var(--olive)"/><path d="M14 14c3-2 9-2 12 0 1 6-2 14-4 14l-2-5-2 5c-2 0-5-8-4-14z" fill="#fff"/></svg></div>Dental</div>
        <div class="icon-item"><div class="icon-box"><svg viewBox="0 0 40 40"><circle cx="16" cy="8" r="4" fill="var(--olive)"/><path d="M12 14h8l2 10-4 10h-4l2-9-4 9H9l3-10z" fill="var(--olive)"/><path d="M24 22h6v12M24 22v12" stroke="var(--ink)" stroke-width="2" fill="none"/></svg></div>Long Term<br>Care</div>
        <div class="icon-item"><div class="icon-box"><svg viewBox="0 0 40 40"><circle cx="12" cy="11" r="4" fill="var(--ink)"/><circle cx="28" cy="11" r="4" fill="var(--ink)"/><circle cx="20" cy="16" r="3.5" fill="var(--olive)"/><rect x="7" y="17" width="10" height="17" rx="2" fill="var(--ink)"/><rect x="23" y="17" width="10" height="17" rx="2" fill="var(--ink)"/><rect x="16" y="21" width="8" height="13" rx="2" fill="var(--olive)"/></svg></div>Life</div>
        <div class="icon-item"><div class="icon-box"><svg viewBox="0 0 40 40"><path d="M5 17a15 11 0 0130 0z" fill="var(--olive)"/><circle cx="14" cy="22" r="3" fill="var(--ink)"/><circle cx="26" cy="22" r="3" fill="var(--ink)"/><rect x="10" y="26" width="8" height="9" fill="var(--ink)"/><rect x="22" y="26" width="8" height="9" fill="var(--ink)"/></svg></div>Family<br>Health</div>
        <div class="icon-item"><div class="icon-box"><svg viewBox="0 0 40 40"><circle cx="20" cy="7" r="4" fill="var(--ink)"/><rect x="16" y="12" width="8" height="22" fill="var(--ink)"/><path d="M4 14h32" stroke="var(--ink)" stroke-width="2"/><path d="M4 24l4-10 4 10zM28 24l4-10 4 10z" fill="var(--olive)"/></svg></div>Liability</div>
        <div class="icon-item"><div class="icon-box"><svg viewBox="0 0 40 40"><path d="M4 36V30h8v-6h8v-6h8v18z" fill="var(--olive)"/><circle cx="28" cy="8" r="3.5" fill="var(--ink)"/><path d="M22 12l8 2 4 6M26 13l-4 6" stroke="var(--ink)" stroke-width="3" fill="none" stroke-linecap="round"/></svg></div>Accident</div>
      </div>
    </section>

    <div class="stripes"><span class="s1"></span><span class="s2"></span></div>
  </section>

  <section class="side-panel side-right">
    <div class="brand-mark">KWR</div>
    <div class="edge-band"></div>
    <div class="vertical-title">ASSOCIATION INSURANCE</div>
    <div class="stripes"><span class="s1"></span><span class="s2"></span></div>
  </section>

</main>
</body>
</html>
```